Website To Serve As A Resource For Medical Conditions

I need a website that is attractive that will be utilized to educate patients on either hepatitis c or HIV so it should be easily readable attractive but also professional. This website is going to be furnished with various topics for example, HIV treatment, HIV and Nutrition, HIV and Exercise, HIV and....

This website will also be cloned and utilized similarly for Hepatitis.

Coded - Design and coding required

1 page

0094D4
00A9DD
6FCCEA
C7EBF8
E9F6FB
A7469A
B969AE
D3A5CF
EDDBEB
F8F0F9
6B429C
8869AF
B7A5CE
E3DAEB
F3F0F8

```html
<!DOCTYPE html>
<html lang="en">
<head>
<meta charset="utf-8">
<title>Vireo — Your Partner In Health &amp; Hope</title>
<link rel="stylesheet" href="https://fonts.googleapis.com/css2?family=Montserrat:wght@600;700;800&family=Inter:wght@400;500;600;700&display=swap">
<style>
:root{
  --blue:#0094D4;
  --blue-light:#00A9DD;
  --purple:#6B429C;
  --purple-mid:#8869AF;
  --ink:#1d1d1f;
  --text:#3b3b3b;
  --footer:#2b2b2b;
  --white:#ffffff;
  --grad:linear-gradient(90deg,#6B429C 0%,#0094D4 100%);
  --grad-band:linear-gradient(100deg,#0094D4 0%,#2a78c8 45%,#6B429C 100%);
}
*{margin:0;padding:0;box-sizing:border-box}
html,body{width:1200px;height:4755px;overflow:hidden;background:var(--white)}
body{position:relative;font-family:'Inter',sans-serif;color:var(--text)}
.abs{position:absolute}
h1,h2,h3,.display{font-family:'Montserrat',sans-serif;color:var(--ink);font-weight:800}
p{font-size:11.5px;line-height:24px}
.btn{position:absolute;width:171px;height:41px;background:var(--grad);color:#fff;font-size:11px;font-weight:700;display:flex;align-items:center;justify-content:center;text-decoration:none}
.brand{display:flex;align-items:center;gap:10px;font-family:'Montserrat',sans-serif;font-weight:800;font-size:24px;color:var(--blue)}
.brand .dot{width:18px;height:18px;border-radius:50%;background:var(--purple)}
.photo{position:absolute}

/* hero */
.hero-panel{left:611px;top:0;width:589px;height:642px;background:linear-gradient(135deg,#0094D4 0%,#1b86cf 50%,#6B429C 100%)}
.nav{position:absolute;top:46px;left:665px;font-size:12px;color:#fff}
.nav a{color:#fff;text-decoration:none;position:absolute;white-space:nowrap}
.hero-title{left:125px;top:208px;font-size:52px;line-height:62px}
.hero-copy{left:125px;top:408px;width:430px}

.quote-card{left:205px;top:642px;width:869px;height:226px;background:#fff;box-shadow:0 6px 30px rgba(0,0,0,.08)}
.quote-dot{width:52px;height:52px;border-radius:50%;background:#fff;display:flex;align-items:center;justify-content:center}
.quote-card .copy{position:absolute;right:374px;top:60px;width:420px;text-align:right}
.quote-card .copy .accent{color:var(--blue);font-weight:700}
.quote-card .rule{position:absolute;left:535px;top:78px;width:1px;height:72px;background:#ddd}
.quote-card .name{position:absolute;right:81px;top:62px;text-align:right;font-size:38px;line-height:46px}

/* about */
.about-bar{left:81px;top:1146px;width:264px;height:445px;background:linear-gradient(180deg,#0094D4,#6B429C)}
.about-img{left:125px;top:965px;width:466px;height:591px;background:linear-gradient(160deg,#e9eef1,#c7cdd4 60%,#8d95a3)}
.sec-title{font-size:40px;line-height:50px}

/* treatments */
.card{position:absolute;width:220px;height:236px;background:#fff;box-shadow:0 4px 26px rgba(0,0,0,.08);text-align:center}
.card .icon{width:74px;height:74px;border-radius:50%;background:linear-gradient(135deg,#0094D4,#4a5fb3);margin:52px auto 0;display:flex;align-items:center;justify-content:center}
.card .label{font-family:'Montserrat',sans-serif;font-weight:700;font-size:16px;line-height:17px;color:#333;margin-top:16px}

/* why */
.why-band{left:0;top:2309px;width:1200px;height:691px;background:var(--grad-band)}
.why-title{left:0;width:1200px;top:2398px;text-align:center;color:#fff;font-size:40px}
.why-copy{left:270px;width:660px;top:2465px;text-align:center;color:#e9f6fb;line-height:27px}
.stat{position:absolute;top:2581px;width:240px;text-align:center;color:#fff}
.stat .num{width:66px;height:66px;margin:0 auto;border-radius:50%;background:#fff;border:4px solid #c7ebf8;display:flex;align-items:center;justify-content:center;font-family:'Montserrat',sans-serif;font-weight:800;font-size:24px;color:var(--blue)}
.stat .lbl{margin-top:18px;font-family:'Montserrat',sans-serif;font-weight:700;font-size:17px;line-height:28px}

/* clients */
.clients{left:125px;top:2819px;width:949px;height:567px;background:#fff;box-shadow:0 6px 30px rgba(0,0,0,.08)}
.clients h2{position:absolute;top:84px;width:100%;text-align:center;font-size:40px}
.review{position:absolute;left:80px;top:188px;width:788px;height:251px;border:1.5px solid var(--purple-mid);text-align:center}
.review h3{font-family:'Inter',sans-serif;font-weight:500;font-size:34px;margin-top:44px}
.review p{font-style:italic;width:620px;margin:14px auto 0;font-size:11px;line-height:25px}
.arrow{position:absolute;top:3118px}

/* news */
.news-img{top:3624px;width:463px;height:325px}
.news-title{top:3990px;font-family:'Inter',sans-serif;font-weight:500;font-size:26px;color:var(--ink)}
.news-copy{top:4046px;width:463px;font-size:10.8px;line-height:25px}

/* footer */
.footer{left:0;top:4377px;width:1200px;height:378px;background:var(--footer);color:#e5e5e5}
.footer p{font-size:11px;color:#ddd}
.footer ul{list-style:none;position:absolute;top:110px;font-size:11px;line-height:24px}
.footer .line{position:absolute;left:0;top:302px;width:1200px;height:1px;background:#555}
.footer .copy{position:absolute;left:0;width:1200px;top:332px;text-align:center;font-size:11px;color:#bbb}
</style>
</head>
<body>

<!-- Hero -->
<div class="abs hero-panel"></div>
<div class="photo" role="img" aria-label="Smiling doctor in white coat holding a clipboard" style="left:700px;top:112px;width:335px;height:530px;background:linear-gradient(180deg,#f2d7c7 0%,#f4f4f4 35%,#e6eef0 70%,#4e9aa0 100%);border-radius:120px 120px 0 0"></div>
<nav class="nav">
  <a style="left:0">About Us</a>
  <a style="left:87px">Treatments</a>
  <a style="left:188px">Testimonials</a>
  <a style="left:296px">Blogs</a>
  <a style="left:363px">Contact</a>
</nav>
<div class="abs brand" style="left:125px;top:40px"><span class="dot"></span>Vireo</div>

<h1 class="abs hero-title">Your Partner<br>In Health &amp;<br>Hope</h1>
<p class="abs hero-copy">Lorem Ipsum is simply dummy text of the printing and typesetting industry. Lorem Ipsum has been the industry's standard dummy text ever since the 1500s,</p>
<a class="btn" style="left:125px;top:515px">Get Started</a>

<div class="abs quote-dot" style="left:589px;top:613px">
  <svg width="30" height="22" viewBox="0 0 30 22"><path d="M2 12a6 6 0 1 1 6 6c0 2-1 3-3 4 5-1 8-5 8-10a7 7 0 0 0-11-4zM16 12a6 6 0 1 1 6 6c0 2-1 3-3 4 5-1 8-5 8-10a7 7 0 0 0-11-4z" fill="#4a5fb3"/></svg>
</div>
<div class="abs quote-card">
  <div class="copy">
    <p>Lorem Ipsum is simply dummy text of the printing and typesetting industry. Lorem Ipsum has been the industry's standard dummy text ever since the 1500s,</p>
    <p class="accent" style="margin-top:4px">Lorem Ipsum is simply dummy</p>
  </div>
  <div class="rule"></div>
  <div class="display name">Dr.<br>Rosalind</div>
</div>

<!-- Who we are -->
<div class="abs about-bar"></div>
<div class="photo about-img" role="img" aria-label="Two lab scientists working with a microscope and sample tubes"></div>
<h2 class="abs sec-title" style="left:641px;top:1063px">Who We Are</h2>
<p class="abs" style="left:641px;top:1129px;width:440px;line-height:27.7px">Lorem Ipsum is simply dummy text of the printing and typesetting industry. Lorem Ipsum has been the industry's standard dummy text ever since the 1500s.Lorem Ipsum is simply dummy text of the printing and typesetting industry. Lorem Ipsum has been the industry's standard dummy text ever since the 1500s.</p>
<p class="abs" style="left:641px;top:1295px;width:440px;line-height:27.7px">Lorem Ipsum is simply dummy text of the printing and typesetting industry. Lorem Ipsum has been the industry's standard dummy text ever since the 1500s</p>
<a class="btn" style="left:641px;top:1408px">Read More</a>

<!-- Treatments -->
<h2 class="abs sec-title" style="left:125px;top:1810px">Treatments<br>We Offer</h2>
<p class="abs" style="left:125px;top:1926px;width:430px;line-height:27.7px">Lorem Ipsum is simply dummy text of the printing and typesetting industry. Lorem Ipsum has been the industry's standard dummy text ever since the 1500s</p>
<a class="btn" style="left:125px;top:2042px">Read More</a>

<div class="card" style="left:611px;top:1715px">
  <div class="icon"><svg width="30" height="34" viewBox="0 0 30 34"><path d="M15 3c-4 0-6 3-6 6 0 3 2 6 4 9l-7 12 4 2 6-10 6 10 4-2-7-12c2-3 4-6 4-9 0-3-2-6-6-6zm0 4c2 0 2 1 2 2 0 2-1 4-2 5-1-1-2-3-2-5 0-1 0-2 2-2z" fill="#fff"/></svg></div>
  <div class="label">HIV<br>Treatment</div>
</div>
<div class="card" style="left:855px;top:1693px">
  <div class="icon"><svg width="32" height="32" viewBox="0 0 32 32"><circle cx="16" cy="17" r="11" fill="#fff"/><path d="M16 6c1-3 4-4 6-3" stroke="#fff" stroke-width="2.5" fill="none"/></svg></div>
  <div class="label">HIV<br>and Nutrition</div>
</div>
<div class="card" style="left:611px;top:1973px">
  <div class="icon"><svg width="28" height="32" viewBox="0 0 28 32"><rect x="4" y="3" width="18" height="26" rx="2" fill="#fff"/><path d="M8 10h10M8 15h10M8 20h6" stroke="#4a5fb3" stroke-width="2"/></svg></div>
  <div class="label">HIV<br>and Exercise</div>
</div>
<div class="card" style="left:855px;top:1949px">
  <div class="icon"><svg width="34" height="34" viewBox="0 0 34 34"><g stroke="#fff" stroke-width="3" stroke-linecap="round"><path d="M17 4v6M17 24v6M4 17h6M24 17h6M8 8l4 4M22 22l4 4M8 26l4-4M22 12l4-4"/></g><circle cx="17" cy="17" r="7" fill="#fff"/></svg></div>
  <div class="label">HIV<br>and Product</div>
</div>

<!-- Why choose us -->
<div class="abs why-band"></div>
<h2 class="abs why-title">Why Choose us</h2>
<p class="abs why-copy">Lorem Ipsum is simply dummy text of the printing and typesetting industry. Lorem Ipsum has been the industry's standard dummy text ever since the 1500s</p>
<div class="stat" style="left:214px"><div class="num">01</div><div class="lbl">Over 20 years of<br>experience.</div></div>
<div class="stat" style="left:471px"><div class="num">02</div><div class="lbl">We have experienced<br>Doctor's.</div></div>
<div class="stat" style="left:737px"><div class="num">03</div><div class="lbl">We are improving<br>everyday.</div></div>

<!-- Clients -->
<div class="abs clients">
  <h2>What Clients Says</h2>
  <div class="review">
    <h3>Mara Quinley</h3>
    <p>Lorem Ipsum is simply dummy text of the printing and typesetting industry. Lorem Ipsum has been the industry's standard dummy text ever since the 1500s, when an unknown printer took a galley of type and scrambled it to make a type specimen book. It has survived not only five centuries, but also the leap into electronic typesetting,</p>
  </div>
  <div class="abs" style="left:448px;top:412px;width:54px;height:54px;border-radius:50%;background:linear-gradient(135deg,#0094D4,#6B429C);display:flex;align-items:center;justify-content:center">
    <svg width="28" height="20" viewBox="0 0 30 22"><path d="M2 12a6 6 0 1 1 6 6c0 2-1 3-3 4 5-1 8-5 8-10a7 7 0 0 0-11-4zM16 12a6 6 0 1 1 6 6c0 2-1 3-3 4 5-1 8-5 8-10a7 7 0 0 0-11-4z" fill="#fff"/></svg>
  </div>
</div>
<svg class="arrow" style="left:158px" width="24" height="32" viewBox="0 0 24 32"><path d="M17 4L6 16l11 12" stroke="#0094D4" stroke-width="4" fill="none"/></svg>
<svg class="arrow" style="left:1018px" width="24" height="32" viewBox="0 0 24 32"><path d="M7 4l11 12L7 28" stroke="#0094D4" stroke-width="4" fill="none"/></svg>

<!-- News -->
<h2 class="abs sec-title" style="left:125px;top:3475px">Latest News And<br>Blogs</h2>
<div class="photo news-img" role="img" aria-label="Doctor checking on a patient resting in a hospital bed" style="left:125px;background:linear-gradient(160deg,#f3f1ee,#d9d2c8 55%,#8a6c55)"></div>
<div class="photo news-img" role="img" aria-label="Doctors measuring a patient's blood pressure" style="left:611px;background:linear-gradient(160deg,#eef2f6,#a9c3dd 50%,#3b6fa8)"></div>
<div class="abs news-title" style="left:125px">Lorem ipsum is a dummy text</div>
<div class="abs news-title" style="left:611px">Lorem ipsum is a dummy text</div>
<p class="abs news-copy" style="left:125px">Lorem Ipsum is simply dummy text of the printing and typesetting industry. Lorem Ipsum has been the industry's standard dummy text ever since the 1500s, when an unknown printer took a galley of type and scrambled it to make a type specimen book. It has survived not only five centuries, but also the leap into electronic typesetting,</p>
<p class="abs news-copy" style="left:611px">Lorem Ipsum is simply dummy text of the printing and typesetting industry. Lorem Ipsum has been the industry's standard dummy text ever since the 1500s, when an unknown printer took a galley of type and scrambled it to make a type specimen book. It has survived not only five centuries, but also the leap into electronic typesetting,</p>
<a class="btn" style="left:125px;top:4218px">Read More</a>
<a class="btn" style="left:611px;top:4218px">Read More</a>

<!-- Footer -->
<footer class="abs footer">
  <div class="abs brand" style="left:125px;top:100px"><span class="dot"></span>Vireo</div>
  <p class="abs" style="left:125px;top:176px;width:340px">Lorem Ipsum is simply dummy text of the printing and typesetting industry.</p>
  <ul style="left:583px"><li>Investors</li><li>Careers</li><li>Media</li><li>Partners</li></ul>
  <ul style="left:735px"><li>Grant Seekers</li><li>Healthcare Professionals</li><li>Business to Business</li><li>Merchandise</li></ul>
  <ul style="left:973px;top:122px"><li>Privacy Statement</li><li>Terms of Use</li><li>Contact Us</li></ul>
  <div class="line"></div>
  <div class="copy">© 2023 Lorem Ipsum. All rights reserved</div>
</footer>

</body>
</html>
```